Heartnight Soiree- The Tailored Gala

This is an elegant Dinner concert event for Valentines day February 14 2020 in Vancouver WA. Live R&B band.

Join us for an Evening of live R&B music Featuring some of Oregon and Washington's talented music artists

Tickets prices: $30 concert only pp
$60 dinner and concert pp
$90 VIP Dinner & one drink/Concert/Premium Seating/Special Gift pp
Doors open @ 6:45 Event is 7:30 to 10:30
Location: Larkspur
417 Fenwick Ave.B Vancouver, WA 98664

www.teamhollowfen.com for more info.

Target Market(s)

Adults /Couples

Industry/Entity Type

Entertainment Industry

Font styles to use
Sans Serif
Decorative

Colors

Designer to choose colors to be used in the design.

Requirements
Must have
• Add the logos for Sponsors of the Event. Brindles is the main sponsor of the event.
• Main colors should be Red and right for valentine. Needs to be sized for a 5x7 Flyer
• Include the pictures of the Music Artists

```html
<!DOCTYPE html>
<html lang="en">
<head>
<meta charset="utf-8">
<title>Heartnight Soiree – The Tailored Gala</title>
<link rel="stylesheet" href="https://fonts.googleapis.com/css2?family=Pinyon+Script&family=Oswald:wght@500;700&family=Roboto+Condensed:wght@400;700&display=swap">
<style>
  :root {
    --ink-dark: #1a0003;
    --wine: #5a0008;
    --crimson: #b3000f;
    --scarlet: #e0101e;
    --rose-text: #ff3345;
    --gold-light: #f6e3a6;
    --gold: #d9b463;
    --gold-deep: #a67a2e;
    --white: #ffffff;
    --photo-a: #6b3b33;
    --photo-b: #2a1410;
  }
  * { margin: 0; padding: 0; box-sizing: border-box; }
  html, body { width: 857px; height: 1200px; overflow: hidden; background: var(--ink-dark); }
  .flyer {
    position: relative;
    width: 857px; height: 1200px; overflow: hidden;
    background: radial-gradient(ellipse 70% 55% at 55% 45%, var(--crimson) 0%, var(--wine) 55%, var(--ink-dark) 100%);
    font-family: "Roboto Condensed", Arial, sans-serif;
    color: var(--white);
  }
  .heart-ornament {
    position: absolute; left: 60px; top: 230px; width: 760px; height: 900px;
    background: radial-gradient(ellipse 50% 45% at 55% 40%, rgba(255,40,50,.55) 0%, rgba(200,0,20,.35) 45%, rgba(90,0,10,0) 75%);
  }
  .gold-text {
    background: linear-gradient(180deg, var(--gold-light) 0%, var(--gold) 50%, var(--gold-deep) 100%);
    -webkit-background-clip: text; background-clip: text; color: transparent;
  }
  .title { position: absolute; left: 40px; top: 20px; font-family: "Pinyon Script", cursive; line-height: 1; }
  .title-line1 { display: block; font-size: 118px; }
  .title-line2 { display: block; font-size: 104px; margin-left: 30px; margin-top: -12px; }
  .title-line3 { display: block; font-size: 78px; margin-top: -4px; }
  .featuring {
    position: absolute; right: 22px; top: 112px; text-align: right;
    font-family: "Oswald", sans-serif; font-weight: 500; font-size: 20px; line-height: 1.3;
    letter-spacing: 1px; color: var(--rose-text); text-transform: uppercase;
  }
  .artist {
    position: absolute; border-radius: 50%;
    background: radial-gradient(circle at 45% 40%, var(--photo-a), var(--photo-b));
    border: 3px solid rgba(0,0,0,.35);
  }
  .artist-1 { left: 595px; top: 236px; width: 174px; height: 174px; }
  .artist-2 { left: 434px; top: 371px; width: 174px; height: 174px; }
  .artist-3 { left: 631px; top: 450px; width: 174px; height: 174px; }
  .artist-4 { left: 516px; top: 563px; width: 184px; height: 184px; }
  .intro { position: absolute; left: 82px; top: 372px; font-size: 27px; line-height: 1.2; }
  .intro strong { font-weight: 700; }
  .tickets-heading {
    position: absolute; left: 82px; top: 458px;
    font-family: "Oswald", sans-serif; font-weight: 700; font-size: 31px; text-transform: uppercase;
  }
  .ticket { position: absolute; left: 82px; display: flex; align-items: center; gap: 14px; }
  .ticket-price { font-family: "Oswald", sans-serif; font-weight: 700; font-size: 72px; line-height: 1; }
  .ticket-detail { font-size: 21px; line-height: 1.35; }
  .ticket-30 { top: 510px; }
  .ticket-60 { top: 592px; }
  .ticket-90 { top: 674px; }
  .event-info { position: absolute; top: 782px; display: flex; align-items: center; gap: 12px; }
  .event-time { left: 80px; }
  .event-place { left: 430px; }
  .event-main { font-family: "Oswald", sans-serif; font-weight: 700; font-size: 34px; line-height: 1.1; text-transform: uppercase; }
  .event-sub { font-size: 19px; }
  .more-info { position: absolute; left: 0; width: 857px; top: 926px; text-align: center; font-size: 21px; }
  .website {
    position: absolute; left: 0; width: 857px; top: 958px; text-align: center;
    font-family: "Oswald", sans-serif; font-weight: 700; font-size: 38px; color: var(--scarlet); text-transform: uppercase;
  }
  .sponsors { position: absolute; left: 30px; right: 30px; top: 1080px; height: 90px; display: flex; justify-content: space-between; align-items: center; }
  .sponsor { font-family: "Oswald", sans-serif; font-weight: 500; display: flex; align-items: center; gap: 10px; }
  .sponsor-salon { font-size: 24px; color: var(--white); }
  .sponsor-main { font-size: 46px; font-weight: 700; color: var(--gold); letter-spacing: 2px; text-transform: uppercase; }
  .sponsor-cheer { font-size: 34px; color: var(--white); text-transform: uppercase; }
  .sponsor-dot { width: 44px; height: 44px; border-radius: 50%; background: var(--white); }
</style>
</head>
<body>
<main class="flyer">
  <div class="heart-ornament" role="img" aria-label="Large swirling red heart ornament with musical flourishes"></div>

  <h1 class="title gold-text">
    <span class="title-line1">Heartnight</span>
    <span class="title-line2">Soiree</span>
    <span class="title-line3">- The Tailored Gala</span>
  </h1>

  <p class="featuring">Featuring some of<br>Oregon and Washington's<br>talented music artists</p>

  <div class="artist artist-1" role="img" aria-label="Portrait of a female vocalist"></div>
  <div class="artist artist-2" role="img" aria-label="Portrait of a female R&amp;B singer"></div>
  <div class="artist artist-3" role="img" aria-label="Portrait of a male artist in a cap"></div>
  <div class="artist artist-4" role="img" aria-label="Portrait of a male singer"></div>

  <p class="intro">Join us for an Evening<br>of live <strong>R&amp;B MUSIC</strong></p>

  <h2 class="tickets-heading">Tickets Prices:</h2>
  <div class="ticket ticket-30"><span class="ticket-price gold-text">$30</span><span class="ticket-detail">Concert only pp</span></div>
  <div class="ticket ticket-60"><span class="ticket-price gold-text">$60</span><span class="ticket-detail">Dinner and concert pp</span></div>
  <div class="ticket ticket-90"><span class="ticket-price gold-text">$90</span><span class="ticket-detail">VIP Dinner &amp; one drink/Concert/<br>Premium Seating/Special Gift pp</span></div>

  <div class="event-info event-time">
    <svg width="52" height="52" viewBox="0 0 52 52" aria-hidden="true">
      <circle cx="26" cy="26" r="22" fill="none" stroke="#d9b463" stroke-width="5"/>
      <path d="M26 13 V27 H36" fill="none" stroke="#d9b463" stroke-width="5" stroke-linecap="round"/>
    </svg>
    <div><div class="event-main">7:30-10:30</div><div class="event-sub">Doors open @ 6:45</div></div>
  </div>

  <div class="event-info event-place">
    <svg width="42" height="56" viewBox="0 0 42 56" aria-hidden="true">
      <path d="M21 3 C10 3 3 11 3 21 C3 34 21 53 21 53 C21 53 39 34 39 21 C39 11 32 3 21 3 Z" fill="none" stroke="#d9b463" stroke-width="5"/>
      <circle cx="21" cy="21" r="6" fill="#d9b463"/>
    </svg>
    <div><div class="event-main">Larkspur</div><div class="event-sub">417 Fenwick Ave.B Vancouver, WA 98664</div></div>
  </div>

  <p class="more-info">For more info:</p>
  <p class="website">www.teamhollowfen.com</p>

  <div class="sponsors">
    <div class="sponsor sponsor-salon">The Marlow Bloom Salon Spa</div>
    <div class="sponsor sponsor-main">Brindles</div>
    <div class="sponsor sponsor-cheer"><span class="sponsor-dot"></span>Cheerline</div>
  </div>
</main>
</body>
</html>
```